Rodent & Wildlife Services from Harborline Termite & Pest Control

I want to show all of the steps in our Rodent/Wildlife Treatment plan:
Inspection- a Harborline wildlife specialist will do a thorough inspection of the Attic and exterior of your home. We will provide you will a detailed Report and Pictures of any infestations found and any areas found to be contaminated. We will also identify any current or potential entry points into the home.
Trapping/Removal- we will create a plan to trap any infestation and remove them- each situation is different and may require a variety of techniques.
Decontamination- animals will leave behind urine, feces, and oils that can potentially contain a variety of bacterias and deseases. We will include in the treatment plan a process to remove and clean up these areas.
Entry Prevention- it is very important to seal up any potential entry points after the infestation has been eliminated. This will help prevent any future infestations into the structure.
Ongoing Protection- Harborline will set up a Rodent baiting program to reduce any surrounding populations.

my thought is to have a picture of each Step and then description (bullet points) about that step

Target Market(s)

Residential

Industry/Entity Type

Pest Control

Font styles to use
Other font styles liked:
• Times Roman

Colors
0455a3
ec1f27

Requirements
Must have
• Professional, concise look.

```html
<!DOCTYPE html>
<html lang="en">
<head>
<meta charset="utf-8">
<title>Harborline Termite &amp; Pest Control – Rodent &amp; Wildlife Services</title>
<link rel="stylesheet" href="https://fonts.googleapis.com/css2?family=Ubuntu:wght@400;500;700&family=Lato:wght@400;700&family=Oswald:wght@600&display=swap">
<style>
  :root{
    --brand-blue:#0455a3;
    --brand-red:#ec1f27;
    --ink:#222;
    --paper:#ffffff;
    --backdrop:#e9e6e1;
  }
  *{box-sizing:border-box;margin:0;padding:0}
  html,body{width:1200px;height:1200px;overflow:hidden;background:var(--backdrop)}
  .flyer{position:absolute;left:152px;top:20px;width:896px;height:1160px;background:var(--paper);overflow:hidden;font-family:"Lato",sans-serif;color:var(--ink)}
  .hero-photo{position:absolute;left:0;top:0;width:896px;height:450px;
    background:linear-gradient(90deg,#f4f5f3 0%,#eef0ea 28%,#b9c7a4 55%,#6f8f4e 75%,#8a7a66 100%)}
  .hero-fade{position:absolute;left:0;top:0;width:520px;height:450px;background:linear-gradient(90deg,rgba(255,255,255,.9),rgba(255,255,255,0))}
  .hero-edge{position:absolute;left:0;top:0}
  .brand-name{position:absolute;left:40px;top:62px;width:240px;font-family:"Ubuntu",sans-serif;font-weight:700;font-size:26px;line-height:1.1;color:var(--brand-red)}
  .headline{position:absolute;left:48px;top:222px;font-family:"Ubuntu",sans-serif;font-weight:500;line-height:1.2}
  .headline span{display:block}
  .headline .l1{font-size:46px;color:var(--brand-blue)}
  .headline .l1 em{font-style:normal;color:var(--brand-red)}
  .headline .l2{font-size:50px;color:var(--brand-red);font-family:"Lato",sans-serif;font-weight:700;letter-spacing:-1px}
  .headline .l3{font-size:46px;color:var(--brand-blue)}
  .badge{position:absolute;border-radius:50%}
  .section-label{position:absolute;left:32px;top:502px;font-family:"Oswald",sans-serif;font-weight:600;font-size:23px;color:var(--brand-red);letter-spacing:-.3px}
  .plan-title{position:absolute;left:32px;top:550px;font-family:"Ubuntu",sans-serif;font-weight:400;font-size:26px;color:var(--brand-blue)}
  .steps{list-style:none;position:absolute;left:32px;top:601px;width:600px}
  .step{position:relative;height:100px}
  .step-thumb{position:absolute;left:0;top:0;width:86px;height:86px;border:2px solid var(--brand-blue);border-radius:8px}
  .step-title{position:absolute;left:101px;top:-3px;font-family:"Ubuntu",sans-serif;font-weight:500;font-size:17.5px;color:var(--brand-blue)}
  .step-text{position:absolute;left:101px;top:20px;font-size:12.8px;line-height:15.8px;text-align:justify}
  .step--inspection .step-text{width:496px}
  .step--trapping .step-title{top:5px}
  .step--trapping .step-text{top:28px;width:357px}
  .step--decon .step-title{top:6px}
  .step--decon .step-text{top:29px;width:432px}
  .step--entry .step-title{top:14px}
  .step--entry .step-text{top:40px;width:468px}
  .step--ongoing .step-title{top:14px}
  .step--ongoing .step-text{top:38px;width:418px}
  .technician{position:absolute;left:650px;top:596px;width:246px;height:564px;border-radius:110px 110px 0 0;z-index:2;
    background:linear-gradient(180deg,#e9c9ae 0%,#e9c9ae 18%,#8e9299 30%,#1f55b8 55%,#1b4ca8 100%)}
  .footer-line{position:absolute;left:0;top:1103px;width:896px;height:6px;background:var(--brand-red)}
  .footer{position:absolute;left:0;top:1116px;width:896px;height:44px;background:var(--brand-blue);color:#fff;font-size:14px}
  .footer span{position:absolute;top:0;height:44px;display:flex;align-items:center;gap:9px}
  .contact-phone{left:41px}
  .contact-web{left:220px}
  .contact-mail{left:423px}
</style>
</head>
<body>
<main class="flyer">
  <div class="hero-photo" role="img" aria-label="Photo of a smiling family sitting on the front lawn of a brick house"></div>
  <div class="hero-fade"></div>

  <svg class="hero-edge" width="896" height="560" viewBox="0 0 896 560" aria-hidden="true">
    <path d="M0 440 L500 440 L560 470 L896 470 L896 560 L0 560 Z" fill="#fff"/>
    <path d="M760 470 C830 450 880 400 896 330 L896 470 Z" fill="#fff"/>
    <rect x="0" y="440" width="480" height="8" fill="#ec1f27"/>
    <rect x="0" y="458" width="470" height="7" fill="#0455a3"/>
    <path d="M760 452 C830 430 878 390 896 320" stroke="#ec1f27" stroke-width="7" fill="none"/>
    <path d="M775 466 C840 445 882 405 896 362" stroke="#0455a3" stroke-width="6" fill="none"/>
  </svg>

  <div class="brand-name">Harborline<br>Termite &amp; Pest Control</div>
  <h1 class="headline">
    <span class="l1">Solutions <em>for</em></span>
    <span class="l2">A HEALTHY</span>
    <span class="l3">Pest-free Life</span>
  </h1>

  <div class="badge" style="left:450px;top:389px;width:196px;height:196px;background:#fff;border:6px solid var(--brand-blue)"></div>
  <div class="badge" role="img" aria-label="Photo of an armadillo caught in a wire cage trap" style="left:460px;top:399px;width:176px;height:176px;background:radial-gradient(circle,#b9aea0,#7d7468);border:4px solid var(--brand-red)"></div>
  <div class="badge" style="left:624px;top:393px;width:182px;height:182px;background:#fff;border:6px solid var(--brand-blue)"></div>
  <div class="badge" role="img" aria-label="Photo of a rat sitting on a loaf of bread" style="left:634px;top:403px;width:162px;height:162px;background:radial-gradient(circle at 50% 40%,#fff 30%,#d9cfc6 70%,#b58a5c);border:4px solid var(--brand-red)"></div>

  <h2 class="section-label">OUR TREATMENT/SERVICE:</h2>
  <h3 class="plan-title">Rodent/Wildlife Treatment plan:</h3>

  <ol class="steps">
    <li class="step step--inspection">
      <div class="step-thumb" role="img" aria-label="Photo of a specialist inspecting under a kitchen cabinet" style="background:linear-gradient(135deg,#c7a27a,#5b6470)"></div>
      <h4 class="step-title">Inspection</h4>
      <p class="step-text">a Harborline wildlife specialist will do a thorough inspection of the Attic and exterior of your home. We will provide you will a detailed Report and Pictures of any infestations found and any areas found to be contaminated. We will also identify any current or potential entry points into the home.</p>
    </li>
    <li class="step step--trapping">
      <div class="step-thumb" role="img" aria-label="Photo of a trap set in an attic" style="background:linear-gradient(135deg,#8b6c4c,#c9c2b6)"></div>
      <h4 class="step-title">Trapping/Removal</h4>
      <p class="step-text">we will create a plan to trap any infestation and remove them- each situation is different and may require a variety of techniques.</p>
    </li>
    <li class="step step--decon">
      <div class="step-thumb" role="img" aria-label="Photo of a worker spraying along a wall" style="background:linear-gradient(180deg,#6d9bd1,#c8d8ea)"></div>
      <h4 class="step-title">Decontamination</h4>
      <p class="step-text">animals will leave behind urine, feces, and oils that can potentially contain a variety of bacterias and deseases. We will include in the treatment plan a process to remove and clean up these areas.</p>
    </li>
    <li class="step step--entry">
      <div class="step-thumb" role="img" aria-label="Photo of sealed entry points around wooden framing" style="background:linear-gradient(90deg,#111,#6a5a3c,#222)"></div>
      <h4 class="step-title">Entry Prevention</h4>
      <p class="step-text">it is very important to seal up any potential entry points after the infestation has been eliminated. This will help prevent any future infestations into the structure.</p>
    </li>
    <li class="step step--ongoing">
      <div class="step-thumb" role="img" aria-label="Photo of a mouse approaching a baited trap" style="background:linear-gradient(135deg,#d4b48c,#7b6248)"></div>
      <h4 class="step-title">Ongoing Protection</h4>
      <p class="step-text">Harborline will set up a Rodent baiting program to reduce any surrounding populations.</p>
    </li>
  </ol>

  <div class="technician" role="img" aria-label="Photo of a smiling pest control technician in blue and grey coveralls holding a sprayer wand"></div>

  <div class="footer-line"></div>
  <footer class="footer">
    <span class="contact-phone"><svg width="18" height="14" viewBox="0 0 18 14" aria-hidden="true"><rect x="1" y="1" width="16" height="12" rx="1" fill="none" stroke="#fff" stroke-width="1.5"/><rect x="4" y="3" width="3" height="8" fill="#fff"/><path d="M9 4h6M9 7h6M9 10h6" stroke="#fff"/></svg>(555) 014-2290</span>
    <span class="contact-web"><svg width="16" height="16" viewBox="0 0 16 16" aria-hidden="true"><circle cx="8" cy="8" r="7" fill="none" stroke="#fff" stroke-width="1.5"/><path d="M1 8h14M8 1c-3 4-3 10 0 14M8 1c3 4 3 10 0 14" stroke="#fff" fill="none"/></svg>www.harborlinetpc.com</span>
    <span class="contact-mail"><svg width="22" height="15" viewBox="0 0 22 15" aria-hidden="true"><rect x="1" y="1" width="20" height="13" rx="1" fill="none" stroke="#fff" stroke-width="1.5"/><path d="M1 1l10 8 10-8" stroke="#fff" stroke-width="1.5" fill="none"/></svg>requests@harborlineTPC.com</span>
  </footer>
</main>
</body>
</html>
```